Simple psychologist website
Open brief, creative designs encouraged
Site map:
Home
our services
our psychologists
selective mutism
resources
contact

Current website:
http://mindsproutyouth.com.au/
Not in love with our logo, or colours etc - open brief
Happy for new font/style/logo for company name - if we choose a logo design from a designer who doesn't win the competition, we will award $50 for the logo and use it in the new website

Website made a few years ago for a sister company that we really like:
http://www.korrelpsychology.com.au/

Clean, credible and warm and friendly look & feel
stock photos OK, designer will be required to hand over any images used in the design as shown in the PSD

Target Market(s)

Adolescents with psychological issues and their families

Industry/Entity Type

Psychology

Number of Pages Required

2 page

Colors

Designer to choose colors to be used in the design.

Requirements
Must have
• One home page - simple with 2 or 3 small areas to tease and attract the user and one template page to suit all the other pages
• We like slides, we want to have 3 slides like korrelpsychology.com.au
• Three slide titles:
• 1. We specialise in many areas, find the right clinical psychologist for your family
• 2. Child Clinical Psychologists in Chatswood and Westmead
• 3. Resources
• Pages structurally similar to
• http://www.korrelpsychology.com.au/
• We like the 'featured' items, which in our case will have splash box titles (can be 3 or 4):
• 1. Selective Mutism
• 2. Is my child anxious?
• 3. Does my child have an eating disorder?
• 4. Parenting adolescents
• Does not need to be a copy of http://www.korrelpsychology.com.au/ and we are willing to accept outside-the-box thinking and design (we in fact encourage it)
• Owner of business wants to highlight Selective Mutism as they have specialists. Consider ways that may make this work.
• Design winner will be based on home page design but winning designer will be required to provide an additional but simpler 'standard' page template design based on the themes used in the winning design.

```html
<!DOCTYPE html>
<html lang="en">
<head>
<meta charset="utf-8">
<title>Mindsprout Youth – Home</title>
<link href="https://fonts.googleapis.com/css2?family=Raleway:wght@400;500;600;700&display=swap" rel="stylesheet">
<style>
:root{
  --navy:#454868;
  --navy-deep:#3a3d5e;
  --ink:#3d4166;
  --lilac:#9b93e3;
  --violet:#a678e0;
  --pale:#eef0fd;
  --footer:#c5cbec;
  --white:#ffffff;
}
*{margin:0;padding:0;box-sizing:border-box}
html,body{width:880px;height:1200px;overflow:hidden}
body{font-family:'Raleway',sans-serif;background:var(--pale);color:var(--ink);position:relative}
.abs{position:absolute}

/* Featured band */
.featured{position:absolute;left:0;top:0;width:880px;height:490px;background:var(--navy)}
.feature-photo{position:absolute;left:160px;top:0;width:272px;height:315px;
  background:radial-gradient(ellipse at 50% 38%,#8a7466 0%,#5d5a6e 40%,#4d4f6e 65%,var(--navy) 100%)}
.lead-title{left:158px;top:244px;font-size:26px;font-weight:500;line-height:31px;color:var(--white);width:300px}
.lead-text{left:158px;top:326px;width:260px;font-size:10.3px;line-height:16px;color:var(--lilac)}
.btn-solid{left:158px;top:399px;width:171px;height:30px;border-radius:15px;background:var(--violet);
  color:var(--white);font-size:11.5px;font-weight:500;display:flex;align-items:center;justify-content:center}
.teaser{position:absolute;left:470px;width:260px}
.teaser h3{font-size:14.5px;font-weight:500;line-height:20px;color:var(--white)}
.teaser p{font-size:10.3px;line-height:16px;color:var(--lilac);margin-top:10px}
.btn-outline{margin-top:14px;width:122px;height:22px;border:1.5px solid var(--violet);border-radius:11px;
  color:var(--white);font-size:10.5px;font-weight:700;display:flex;align-items:center;justify-content:center}

/* Team */
.team-title{left:0;width:880px;top:544px;text-align:center;font-size:24px;font-weight:500;color:var(--ink)}
.team-intro{left:0;width:880px;top:595px;text-align:center;font-size:10px;line-height:16px;color:var(--ink)}
.member{position:absolute;top:645px;width:133px}
.member-photo{width:133px;height:195px;background:linear-gradient(160deg,#a9a9ad 0%,#8d8b8c 45%,#6f6e72 100%)}
.member-name{margin-top:17px;font-size:14.5px;line-height:20px;font-weight:500;color:var(--ink)}
.member-role{margin-top:14px;font-size:7.6px;color:var(--ink)}
.member-rule{margin-top:14px;width:33px;height:3px;background:var(--ink)}

/* Footer */
.site-footer{position:absolute;left:0;top:998px;width:880px;height:202px;background:var(--footer)}
.foot-col{position:absolute;top:58px;font-size:10px;line-height:16px;color:var(--ink)}
.foot-col b{font-weight:700}
.foot-col .gap{height:10px}
</style>
</head>
<body>

<section class="featured">
  <div class="feature-photo" role="img" aria-label="Portrait photo of a young child with curly hair, fading into the background"></div>
  <h1 class="abs lead-title">Selective Mutism In Children</h1>
  <p class="abs lead-text">Elena Varga, Clinical Psychologist at Mindsprout Youth has many years of working with children with selective mutism. She is currently also ...</p>
  <a class="abs btn-solid">Read More</a>

  <article class="teaser" style="top:40px">
    <h3>Why Is My Child Anxious?</h3>
    <p>Lorem ipsum dolor sit amet, consectetur adipiscing elit, sed do eut labore et dolore magna aliqua ...</p>
    <div class="btn-outline">Read More</div>
  </article>
  <article class="teaser" style="top:176px">
    <h3>Does My Child Have An<br>Eating Disorder?</h3>
    <p>Lorem ipsum dolor sit amet, consectetur adipiscing elit, sed do eut labore et dolore magna aliqua ...</p>
    <div class="btn-outline">Read More</div>
  </article>
  <article class="teaser" style="top:332px">
    <h3>Parenting Adolescents</h3>
    <p>Lorem ipsum dolor sit amet, consectetur adipiscing elit, sed do eut labore et dolore magna aliqua ...</p>
    <div class="btn-outline">Read More</div>
  </article>
</section>

<h2 class="abs team-title">Meet Our Psychologists</h2>
<p class="abs team-intro">Lorem ipsum dolor sit amet, consectetur adipiscing elit, sed do<br>eiusmod tempor incididunt ut labore et dolore magna aliqua.</p>

<div class="member" style="left:128px">
  <div class="member-photo" role="img" aria-label="Portrait photo of a psychologist"></div>
  <div class="member-name">Thomas<br>Ashdown</div>
  <div class="member-role">Specialist in child Psychology</div>
  <div class="member-rule"></div>
</div>
<div class="member" style="left:291px">
  <div class="member-photo" role="img" aria-label="Portrait photo of a psychologist"></div>
  <div class="member-name">Thomas<br>Ashdown</div>
  <div class="member-role">Specialist in child Psychology</div>
  <div class="member-rule"></div>
</div>
<div class="member" style="left:454px">
  <div class="member-photo" role="img" aria-label="Portrait photo of a psychologist"></div>
  <div class="member-name">Thomas<br>Ashdown</div>
  <div class="member-role">Specialist in child Psychology</div>
  <div class="member-rule"></div>
</div>
<div class="member" style="left:618px">
  <div class="member-photo" role="img" aria-label="Portrait photo of a psychologist"></div>
  <div class="member-name">Thomas<br>Ashdown</div>
  <div class="member-role">Specialist in child Psychology</div>
  <div class="member-rule"></div>
</div>

<footer class="site-footer">
  <div class="foot-col" style="left:138px">
    <div><b>Phone:</b> 0412 555 018</div>
    <div class="gap"></div>
    <div><b>Fax:</b> (02) 9555 0147</div>
    <div class="gap"></div>
    <div><b>Email:</b> info@<br>mindsproutyouth.com.au</div>
  </div>
  <div class="foot-col" style="left:291px">
    <div><b>Westmead</b></div>
    <div class="gap"></div>
    <div>Suite 204, level 2<br>Parkside Health Centre<br>88 Larkin Road<br>Westmead NSW 2145</div>
  </div>
  <div class="foot-col" style="left:454px">
    <div><b>Chatswood</b></div>
    <div class="gap"></div>
    <div>Suite 14C,<br>5-7 Willow Lane<br>Chatswood NSW 2067</div>
  </div>
  <div class="foot-col" style="left:618px">
    <div><b>Postal Address</b></div>
    <div class="gap"></div>
    <div>Mindsprout<br>PO Box 512<br>Westmead NSW 2145</div>
  </div>
</footer>

</body>
</html>
```